Digital Marketing Agency Needs a Pagecraft Web Design

We need a web design for a new company based in Evergreen, Colorado (the greater Denver Metro area) called "Copper Wayfarer". We are a full service Digital Marketing Agency that offers and provides the following services to clients: Website Design, Search Engine Optimization, Plexo Local Listing, Local Online Directories, Reputation Marketing, Social Media Marketing, Video Marketing, Pay Per Click. Our slogan is "Digital Marketing, Elevated!" We want a PageCraft web design that has a very modern look. We would like to see designs use the following colors (included color code):

light blue (#0cb9ea)
orange (#f47528)
white (#ffffff)
black (#000000).

These colors coincide with the colors of our logo (attached). We prefer a flat design but would like some elements of depth. We need a header that includes a logo (attached), name/address/phone number of our company, a contact call-to-action button (these need to be very easy to locate on the page), menu bar, and banner (very flexible to set up of banner).. The footer needs to include logo, NAP, Footer Menu, Section for blogs (includes title of blog that links to post), & copyright. We also need a way to prominently display and link our key featured services (Website Design, Search Engine Optimization, Plexo Local Listing, Local Online Directories, Reputation Marketing, Social Media Marketing, Video Marketing, Pay Per Click).

Here are three websites that we really like and would like to see certain elements incorporated:

1. http://quillstonemedia.example/ (like how the services were laid out on the home page for services -- "Features" section... want to follow this same type of idea, just in our own way).
2. http://tavenmark.example/ (love the modern, visual aspect of this site and how professionally clean it is.... very easy to understand and navigate through).
3. http://norvacreative.example/ (like how this site incorporates interactive features that engage people while visiting the site).

The overall goal of the site is to effectively emphasize the services we provide (see above), who we are, and how to contact us for services.

** Any stock photos used HAVE TO BE TAKEN from Lumafold Pictures (http://www.lumafoldpics.example/). And if watermarked, please provide the image code for each image used.

Target Market(s)

Lawyers, Insurance agents, Real Estate, Restaurant Owners, Doctors and all other medical providers.

Industry/Entity Type

Internet

Number of Pages Required

1 page

Font styles to use
Serif

Colors
33a6d7
ffffff
000000
f37122

Requirements
Must have
• 1. Header w/ Logo, Name/Address/Phone Number of our business, a call-to-action button to "Contact us":
• Copper Wayfarer – Digital Marketing
• 41872 Cobblewick Drive
• Evergreen, CO 80439
• 303-547-9183
• 2. Navigation Menu
• 3. Some type of banner
• 4. Featured Services section (with a short blurb about each)
• 5. Contact Form (somewhere above the fold)
• 6. Need at least 2-3 paragraphs of text (use dummy text) somewhere on the page (either in full or in sections)....
• 7. Footer that includes logo, NAP (see above), Menu Links, Links for services (see above), Blog Section, Social Media icons (Chatterly, Peepline, Plexo+, and ReelHub) & a copyright.
Nice to have
• Here are three websites that we really like and would be nice to see elements of incorporated:
• 1. http://quillstonemedia.example/ (like how the services were laid out on the home page -- "Features" section... want to follow this same type of idea, just in our own way).
• 2. http://tavenmark.example/ (love the modern, visual aspect of this site and how professionally clean it is.... very easy to understand and navigate through).
• 3. http://norvacreative.example/ (like how this site incorporates interactive features that engage people that visit the site).
Should not have
• Pretty flexible... We just need to make sure it's a Pagecraft web design.

```html
<!DOCTYPE html>
<html lang="en">
<head>
<meta charset="utf-8">
<title>Copper Wayfarer – Digital Marketing, Elevated!</title>
<link href="https://fonts.googleapis.com/css2?family=Open+Sans:wght@400;600;700;800&display=swap" rel="stylesheet">
<style>
:root{
  --blue:#0cb9ea;
  --teal:#2bb3c9;
  --teal-dark:#1a8ea3;
  --orange:#f47528;
  --ink:#000000;
  --dark:#232323;
  --dark-2:#2e2e2e;
  --grey:#7a7a7a;
  --light:#ececec;
  --white:#ffffff;
}
*{box-sizing:border-box;margin:0;padding:0}
html,body{width:716px;height:1200px;overflow:hidden;background:var(--white)}
body{font-family:"Open Sans",Arial,sans-serif;color:var(--grey);position:relative}
.topbar{height:20px;background:var(--dark);display:flex;justify-content:space-between;align-items:center;padding:0 34px;font-size:8px;color:#cfcfcf}
.topbar span{margin-right:16px}
.topbar .dot{display:inline-block;width:6px;height:6px;border-radius:50%;background:var(--orange);margin-right:4px;vertical-align:middle}
.header{height:52px;display:flex;justify-content:space-between;align-items:center;padding:0 34px}
.brand{display:flex;align-items:center;gap:8px}
.brand-mark{width:24px;height:24px;border-radius:50%;background:var(--orange)}
.brand-name{font-weight:800;font-size:21px;color:var(--orange);line-height:1}
.brand-tag{font-size:8px;color:var(--grey);margin-top:2px}
.nap{text-align:right;font-size:8px;line-height:1.35;color:var(--grey)}
.nap .phone{font-size:17px;font-weight:700;color:var(--orange);line-height:1.1}
.nav{height:18px;background:var(--dark);display:flex;align-items:center;padding:0 34px;gap:20px}
.nav a{color:var(--white);font-size:8px;font-weight:600;text-decoration:none;letter-spacing:.3px}
.banner{height:321px;background:var(--teal);position:relative;text-align:center}
.banner h1{padding-top:34px;font-size:25px;font-weight:700;color:var(--white);letter-spacing:.5px}
.banner-art{position:absolute;left:108px;top:80px;width:500px;height:180px;border-radius:6px;background:radial-gradient(circle at 50% 55%,#f7a35c 0,#f47528 18%,#7fd3e0 42%,var(--teal) 75%)}
.banner-band{position:absolute;left:0;right:0;bottom:0;height:56px;background:var(--teal-dark);display:flex;align-items:center;justify-content:center;font-size:22px;font-weight:800;color:var(--white);letter-spacing:.6px}
.features{height:207px;background:repeating-linear-gradient(45deg,#e3e3e3 0 2px,#ebebeb 2px 5px);display:flex;align-items:center;padding:0 14px 0 0}
.features-tab{width:38px;height:168px;background:var(--blue);display:flex;align-items:center;justify-content:center}
.features-tab span{transform:rotate(-90deg);color:var(--white);font-weight:800;font-size:15px;letter-spacing:2px;white-space:nowrap}
.feature-list{display:flex;gap:6px;margin-left:8px}
.feature{width:79px;background:var(--white);box-shadow:0 1px 2px rgba(0,0,0,.15)}
.feature-img{height:104px;background:#d4d4d4;display:flex;align-items:center;justify-content:center;text-align:center;font-size:9px;font-weight:600;color:#9a9a9a;line-height:1.3}
.feature p{padding:7px 6px 9px;font-size:7.5px;color:var(--blue);line-height:1.35;height:56px}
.intro{display:flex;padding:26px 40px 0 40px;gap:40px;height:233px}
.intro h2{font-size:21px;font-weight:600;color:var(--blue)}
.intro h2 em{font-style:normal;color:var(--orange)}
.about{width:320px}
.about p{font-size:9px;line-height:1.5;margin-top:10px}
.testimonials{flex:1;position:relative}
.dots{position:absolute;right:0;top:8px;display:flex;gap:4px}
.dots i{width:8px;height:8px;border-radius:50%;background:#444}
.dots i:last-child{background:var(--orange)}
.quote{display:flex;gap:10px;margin-top:12px}
.quote b{font-size:40px;color:#bbb;line-height:.9;font-family:Georgia,serif}
.quote p{font-size:9px;line-height:1.5}
.author{text-align:right;font-size:9px;color:var(--orange);font-weight:600;margin-top:4px}
.contact{height:140px;background:var(--orange);position:relative;padding:28px 40px 0}
.contact-map{position:absolute;right:40px;top:10px;width:360px;height:120px;border-radius:50%;background:radial-gradient(ellipse at center,rgba(255,255,255,.16),rgba(255,255,255,0) 70%)}
.contact h2{position:relative;font-size:21px;font-weight:800;color:var(--white);letter-spacing:.6px}
.contact-form{position:relative;display:flex;gap:22px;margin-top:26px;align-items:flex-end}
.field{width:130px;border-bottom:1px solid rgba(255,255,255,.8);font-size:9px;color:var(--white);padding-bottom:4px}
.submit{margin-left:auto;border:1px solid var(--white);color:var(--white);font-size:8px;font-weight:700;padding:5px 22px;letter-spacing:.6px}
.footer{position:absolute;left:0;top:990px;width:716px;height:210px;background:var(--dark-2);color:#bdbdbd}
.footer-brand{position:absolute;left:40px;top:36px}
.footer-brand .brand-name{font-size:20px}
.footer-brand .brand-tag{color:#9a9a9a}
.col-title{display:flex;align-items:center;gap:8px;font-size:9px;font-weight:700;color:var(--orange)}
.col-title::before,.col-title::after{content:"";height:1px;width:36px;background:#555}
.links{position:absolute;left:284px;top:22px;width:160px}
.links ul{list-style:none;columns:2;margin-top:10px;font-size:8px;line-height:1.8;padding-left:10px}
.social{display:flex;gap:5px;margin:12px 0 0 36px}
.social i{width:16px;height:16px;display:block}
.blog{position:absolute;left:480px;top:22px;width:200px}
.blog ul{list-style:none;margin-top:10px;font-size:7.5px;line-height:1.35}
.blog li{margin-bottom:7px}
.blog time{display:block;color:var(--blue);font-weight:600}
.copyright{position:absolute;left:0;right:0;top:150px;text-align:center;font-size:8px;color:#9a9a9a}
.to-top{position:absolute;left:343px;top:170px;text-align:center;font-size:6px;color:#9a9a9a}
.to-top svg{display:block;margin:0 auto 2px}
</style>
</head>
<body>
<div class="topbar">
  <div><span><i class="dot"></i>303-547-9183</span><span><i class="dot"></i>info@copperwayfarer.example</span></div>
  <div>Language : EN</div>
</div>

<header class="header">
  <div class="brand">
    <div class="brand-mark"></div>
    <div><div class="brand-name">Copper Wayfarer</div><div class="brand-tag">Digital Marketing, Elevated!</div></div>
  </div>
  <div class="nap">
    <div class="phone">(303) 547-9183</div>
    <div>Copper Wayfarer – Digital Marketing</div>
    <div>41872 Cobblewick Drive, Evergreen, CO 80439</div>
  </div>
</header>

<nav class="nav">
  <a href="#">HOME</a><a href="#">ABOUT</a><a href="#">SERVICES</a><a href="#">TEAM</a><a href="#">WORK</a><a href="#">BLOG</a><a href="#">CONTACT</a>
</nav>

<section class="banner">
  <h1>DIGITAL MARKETING TRENDS FOR 2015</h1>
  <div class="banner-art" role="img" aria-label="Flat illustration of a megaphone surrounded by marketing icons over a city skyline"></div>
  <div class="banner-band">DRIVING DIGITAL PERFORMANCE.</div>
</section>

<section class="features">
  <div class="features-tab"><span>FEATURES</span></div>
  <div class="feature-list">
    <article class="feature"><div class="feature-img">NO<br>IMAGE</div><p>Website Design Built for Your Business</p></article>
    <article class="feature"><div class="feature-img">NO<br>IMAGE</div><p>Search Engine Optimization That Ranks</p></article>
    <article class="feature"><div class="feature-img">NO<br>IMAGE</div><p>Plexo Local Listing Setup and Care</p></article>
    <article class="feature"><div class="feature-img">NO<br>IMAGE</div><p>Local Online Directories Done Right</p></article>
    <article class="feature"><div class="feature-img">NO<br>IMAGE</div><p>Reputation Marketing for Trusted Brands</p></article>
    <article class="feature"><div class="feature-img">NO<br>IMAGE</div><p>Social Media Marketing That Engages</p></article>
    <article class="feature"><div class="feature-img">NO<br>IMAGE</div><p>Video Marketing to Tell Your Story</p></article>
    <article class="feature"><div class="feature-img">NO<br>IMAGE</div><p>Pay Per Click With Clear Returns</p></article>
  </div>
</section>

<section class="intro">
  <div class="about">
    <h2>About <em>Copper Wayfarer</em></h2>
    <p>Donec sollicitudin molestie malesuada. Vestibulum ante ipsum primis in faucibus orci luctus et ultrices posuere cubilia curae.</p>
    <p>Sed auctor sit amet aliquam nisl, ullamcorper sit amet ligula. Donec rutrum congue leo eget malesuada.</p>
    <p>Vivamus suscipit tortor eget felis porttitor volutpat. Curabitur arcu erat, accumsan id imperdiet et, porttitor at sem.</p>
  </div>
  <div class="testimonials">
    <h2>Testimonials</h2>
    <div class="dots"><i></i><i></i><i></i></div>
    <div class="quote"><b>“</b><p>Donec sollicitudin molestie malesuada. Vestibulum ante ipsum primis in faucibus orci luctus et ultrices posuere cubilia curae nulla.</p></div>
    <div class="author">John Doe</div>
  </div>
</section>

<section class="contact">
  <div class="contact-map" role="img" aria-label="Faint world map texture"></div>
  <h2>GET IN TOUCH WITH US</h2>
  <form class="contact-form">
    <div class="field">Full Name</div>
    <div class="field">Phone Number</div>
    <div class="field">Email</div>
    <div class="submit">SUBMIT</div>
  </form>
</section>

<footer class="footer">
  <div class="footer-brand">
    <div class="brand">
      <div class="brand-mark"></div>
      <div><div class="brand-name">Copper Wayfarer</div><div class="brand-tag">Digital Marketing, Elevated!</div></div>
    </div>
  </div>
  <div class="links">
    <div class="col-title">QUICK LINKS</div>
    <ul><li>Home</li><li>About</li><li>Services</li><li>Team</li><li>Work</li><li>Blog</li><li>Contact</li></ul>
    <div class="social" aria-label="Chatterly, Peepline, Plexo+, ReelHub">
      <i style="background:var(--blue)"></i><i style="background:#3b5b98"></i><i style="background:#d34836"></i><i style="background:var(--orange)"></i>
    </div>
  </div>
  <div class="blog">
    <div class="col-title">BLOG</div>
    <ul>
      <li><time>Jan 12, 2015</time>Five Local SEO Tips for Lawyers</li>
      <li><time>Jan 20, 2015</time>Why Reviews Matter for Restaurants</li>
      <li><time>Feb 03, 2015</time>Video Marketing Ideas for Doctors</li>
    </ul>
  </div>
  <div class="copyright">©2015 Copper Wayfarer. All rights reserved.</div>
  <div class="to-top">
    <svg width="16" height="16" viewBox="0 0 16 16"><circle cx="8" cy="8" r="7.5" fill="none" stroke="#9a9a9a"/><path d="M5 9.5 8 6.5 11 9.5" fill="none" stroke="#9a9a9a" stroke-width="1.4"/></svg>
    To Top
  </div>
</footer>
</body>
</html>
```